Website for the new investment company.

We are building a website for a new company. This will be an investment company. The name of the company is Tern Harbor Equity, or THE. We don't have a company logo yet, so happy to take suggestions on that as well (and will add that to the final cost). The investors of this company will exclusively be Dunmore College alumni graduates. The investors are not students, but instead older professionals in various industries, that previously graduated from the Dunmore College. This company will establish an investment fund and invest in multiple businesses.
The purpose of the website will be to educate Dunmore alumni on the investment fund.
We are looking for:
1. The design to be relatable, but not the copy of the Dunmore College website. https://www.dunmorecol.edu/
2. This is an investment website and must mimic other similar websites
https://plovergate-fund.com/
https://www.brindlevest.com/
https://kestowholdings.com/site/global/home/p_home.gsp
3. Project timeline. We are focused on receiving a design in the next two weeks and then finishing the website over the following 2 weeks. We anticipate paying for additional work and customization after the designs are provided.
4. Website Pages:
1) Homepage - Mission and Objective (high quality photos along with text that we will provide after selecting the winning design)
2) Background - Text and biographies on the 2 founders (high quality photos along with text that we will provide after selecting the winning design)
3) Advisory Board - Text and biographies on the investment Fund's 3 advisory board members (high quality photos along with text that we will provide after selecting the winning design)
4) Fund I - Text and information on the specific investment fund including pictures and biographies of the investment committee (high quality photos along with text that we will provide after selecting the winning design)
5) Contact Us - Typical website contact page for visitors

Target Market(s)

Dunmore Alumni graduates

Industry/Entity Type

Investment

Coding

Coded - Design and coding required

Font styles to use
Serif
Sans Serif

Colors
0054AA
0677BA
7BADD7
CADEEF
E8F1F8

Requirements
Must have
• Must look like other private investment websites as provided in project description
Nice to have
• Mimics the Dunmore College style, but definitely needs to be different. This company has no direct relationship with Dunmore College.
Should not have
• No commercial transactions, no credit card payments etc. Do not replicate any logos, designs or proprietary content from Dunmore College.

```html
<!DOCTYPE html>
<html lang="en">
<head>
<meta charset="utf-8">
<title>Tern Harbor Equity</title>
<link rel="stylesheet" href="https://fonts.googleapis.com/css2?family=Outfit:wght@300;400;500;600&display=swap">
<style>
:root{
  --navy:#0b4a7f;
  --navy-deep:#0a2b4c;
  --ink:#0b4a86;
  --accent:#3f88d9;
  --sky:#7badd7;
  --mist:#cadeef;
  --frost:#e8f1f8;
  --text:#33404d;
  --white:#ffffff;
}
*{margin:0;padding:0;box-sizing:border-box}
html,body{width:1200px;height:4040px;overflow:hidden}
body{font-family:"Outfit",sans-serif;color:var(--text);background:var(--white);position:relative}
section,header,footer{position:absolute;left:0;width:1200px}
.abs{position:absolute}
.brand{font-family:"Outfit",sans-serif;font-weight:600;color:var(--accent);text-transform:uppercase;letter-spacing:1px;line-height:1.15;display:flex;align-items:center;gap:14px}
.brand-mark{width:22px;height:22px;border:2px solid var(--accent);border-radius:50%}

/* hero */
.hero{top:0;height:706px;background:linear-gradient(180deg,#161d2b 0%,#202a3d 45%,#1a2334 100%)}
.hero-photo{position:absolute;inset:0;background:radial-gradient(ellipse at 50% 40%,rgba(70,80,100,.55),rgba(15,20,32,.2) 70%)}
.hero .brand{left:105px;top:58px;font-size:23px}
.nav{right:108px;top:76px;display:flex;gap:26px;font-size:11px;font-weight:500;letter-spacing:.6px;text-transform:uppercase}
.nav a{color:var(--accent);text-decoration:none}
.nav a.current{color:var(--white)}
.eyebrow{display:flex;align-items:center;gap:14px;font-size:12.5px;color:var(--accent);text-transform:uppercase;letter-spacing:.3px}
.eyebrow::before,.eyebrow::after{content:"";width:36px;height:1px;background:var(--accent)}
.hero .eyebrow{left:0;width:1200px;justify-content:center;top:272px}
.hero h1{left:0;width:1200px;top:296px;text-align:center;color:var(--white);font-weight:300;font-size:56px;line-height:64px;letter-spacing:.3px}
.btn-outline{left:518px;top:444px;width:165px;height:39px;border:1.5px solid var(--accent);color:var(--mist);font-size:12px;letter-spacing:2px;display:flex;align-items:center;justify-content:center;text-transform:uppercase}
.scroll{left:570px;top:620px;width:60px;text-align:center;font-size:9px;color:#9fb0c4;letter-spacing:.5px}
.social-side{left:1150px;top:258px;width:40px;display:flex;flex-direction:column;align-items:center;gap:8px}
.social-side .label{writing-mode:vertical-rl;transform:rotate(180deg);font-size:9px;font-weight:600;color:#c8d2de;letter-spacing:1px;margin-bottom:6px}
.dot-ico{width:16px;height:16px;border:1px solid #c8d2de;border-radius:50%}

/* section labels */
.tag{display:flex;align-items:center;gap:12px;font-size:12.5px;color:var(--accent);text-transform:uppercase}
.hex{width:46px;height:50px}
h2.lead{font-weight:400;color:var(--ink);font-size:30px;line-height:34px}

/* background */
.background{top:706px;height:749px}
.background .tag{left:105px;top:91px}
.background h2{left:107px;top:186px;width:420px}
.background .copy{left:107px;top:340px;width:360px;font-size:14px;line-height:18.3px;color:#2e3640}
.background .copy p+p{margin-top:16px}
.btn-solid{background:var(--navy);color:var(--white);font-size:11.5px;letter-spacing:1.6px;display:flex;align-items:center;justify-content:center;text-transform:uppercase}
.background .btn-solid{left:105px;top:526px;width:141px;height:34px}
.dots{left:490px;top:456px;width:30px;height:90px;background-image:radial-gradient(#9aa8b8 1px,transparent 1.4px);background-size:20px 20px}
.photo-a{left:533px;top:91px;width:331px;height:494px;background:linear-gradient(160deg,#dfeef8 0%,#7badd7 45%,#2f7fbf 70%,#cfe4f3 100%)}
.pale-a{left:632px;top:212px;width:303px;height:408px;background:var(--frost)}
.photo-b{left:868px;top:282px;width:262px;height:374px;background:linear-gradient(200deg,#d7e9f7 0%,#a9cbe8 55%,#3a4656 100%)}

/* values */
.values{top:1455px;height:748px;background:var(--navy)}
.values .tag{left:0;width:1200px;justify-content:center;top:90px;color:#8fb4dc}
.values h2{left:0;width:1200px;text-align:center;top:183px;color:#cfe0f1;font-weight:300;font-size:30px}
.ring-outer{left:409px;top:270px;width:382px;height:382px;border:1px dashed rgba(143,180,220,.45);border-radius:50%}
.ring-inner{left:430px;top:291px;width:340px;height:340px;border-radius:50%;background:#124f88}
.ring-name{left:430px;top:291px;width:340px;height:340px;display:flex;align-items:center;justify-content:center;text-align:center;color:var(--accent);font-size:26px;font-weight:500;line-height:32px;text-transform:uppercase;letter-spacing:1px}
.value{display:flex;align-items:center;gap:16px;color:#b9cfe6;font-size:16px;font-weight:300;letter-spacing:.3px}
.value svg{width:72px;height:78px;flex:none}
.value.left{flex-direction:row;justify-content:flex-end}

/* mission */
.mission{top:2203px;height:775px}
.mission .tag{left:105px;top:163px}
.mission h2{left:107px;top:270px;width:390px}
.photo-c{left:546px;top:162px;width:355px;height:516px;background:linear-gradient(150deg,#b8dcf1 0%,#4e9dd0 40%,#1d5c8f 70%,#c7e2f3 100%)}
.photo-d{left:904px;top:91px;width:190px;height:353px;background:linear-gradient(170deg,#5c6776 0%,#d9dde2 40%,#e6c9bf 75%,#f1ece8 100%)}

/* contact */
.contact{top:2978px;height:636px;background:linear-gradient(180deg,#1b3556 0%,#25456d 50%,#1c3a5f 100%)}
.contact .tag{left:0;width:1200px;justify-content:center;top:94px;color:#c7d6e7}
.contact h2{left:0;width:1200px;text-align:center;top:188px;color:var(--white);font-weight:300;font-size:30px}
.field{height:44px;border-bottom:1px solid rgba(160,185,215,.35);background:rgba(16,40,70,.25);color:#c7d3e2;font-size:14px;padding:12px 16px}
.field.msg{height:88px}
.contact .btn-solid{left:529px;top:510px;width:141px;height:34px;background:#0c4d8e}

/* footer */
.site-footer{top:3614px;height:426px;background:var(--navy)}
.site-footer .brand{left:149px;top:110px;font-size:23px}
.f-social{left:216px;top:208px;display:flex;gap:12px}
.f-social span{width:20px;height:20px;border:1.5px solid #cfe0f1;border-radius:50%}
.f-col h4{font-size:12px;font-weight:600;color:var(--white);letter-spacing:.6px;text-transform:uppercase;padding-bottom:12px;border-bottom:1px solid rgba(143,180,220,.3);margin-bottom:12px}
.f-col p,.f-col li{font-size:10.5px;line-height:17px;color:#9dbbdc;list-style:none}
.f-row{display:flex;gap:8px;margin-bottom:12px}
.f-row svg{flex:none;margin-top:3px}
.subscribe{margin-top:12px;width:181px;height:30px;border:1px solid var(--sky);display:flex;align-items:center;justify-content:space-between;padding:0 10px;font-size:10px;color:#cfe0f1}
.f-rule{left:105px;top:329px;width:990px;height:1px;background:rgba(143,180,220,.3)}
.to-top{left:1122px;top:307px;width:44px;height:44px;border:1px solid var(--sky);display:flex;align-items:center;justify-content:center}
.copyright{left:0;width:1200px;top:351px;text-align:center;font-size:9.5px;font-weight:600;color:var(--accent);letter-spacing:.3px}
</style>
</head>
<body>

<header class="hero">
  <div class="hero-photo" role="img" aria-label="Group photo of smiling professionals in business suits, darkened under a navy overlay"></div>
  <div class="abs brand"><span class="brand-mark"></span><span>Tern Harbor<br>Equity</span></div>
  <nav class="abs nav">
    <a class="current" href="#">Home</a><a href="#">Background</a><a href="#">Advisory Board</a><a href="#">Investment</a><a href="#">Contact</a>
  </nav>
  <div class="abs eyebrow">Welcome to Tern Harbor Equity</div>
  <h1 class="abs">Bringing Dunmore College Alumni<br>Graduates to Investment Fund</h1>
  <div class="abs btn-outline">Learn More</div>
  <div class="abs scroll">
    <svg width="16" height="40" viewBox="0 0 16 40"><rect x="2" y="1" width="12" height="19" rx="6" fill="none" stroke="#9fb0c4" stroke-width="1.2"/><line x1="8" y1="6" x2="8" y2="10" stroke="#9fb0c4" stroke-width="1.2"/><line x1="8" y1="24" x2="8" y2="34" stroke="#9fb0c4"/><path d="M5 31l3 3 3-3" fill="none" stroke="#9fb0c4"/></svg>
    <div>SCROLL</div>
  </div>
  <div class="abs social-side"><span class="label">BE SOCIAL ·····</span><span class="dot-ico"></span><span class="dot-ico"></span><span class="dot-ico"></span></div>
</header>

<section class="background">
  <div class="abs tag">
    <svg class="hex" viewBox="0 0 46 50"><polygon points="23,2 43,13.5 43,36.5 23,48 3,36.5 3,13.5" fill="var(--frost)" stroke="var(--mist)" stroke-width="2"/><rect x="17" y="17" width="12" height="16" fill="none" stroke="var(--accent)" stroke-width="2"/></svg>
    <span>/ Background</span>
  </div>
  <h2 class="abs lead">Tern Harbor Equity is an investment company, exclusively for Dunmore College alumni graduates.</h2>
  <div class="abs copy">
    <p>Lorem ipsum dolor sit amet, consectetur adipiscing elit, sed do eiusmod tempor incididunt ut labore et dolore magna aliqua. Ut enim ad minim veniam, quis nostrud exercitation ullamco laboris nisi ut aliquip ex ea commodo consequat.</p>
    <p>Duis aute irure dolor in reprehenderit in voluptate velit esse cillum dolore eu fugiat nulla pariatur. Exce teur sint occaecat cupidatat non proident.</p>
  </div>
  <div class="abs btn-solid">Learn More</div>
  <div class="abs dots"></div>
  <div class="abs pale-a"></div>
  <div class="abs photo-a" role="img" aria-label="Business hand touching a glowing blue chart with a rising arrow"></div>
  <div class="abs photo-b" role="img" aria-label="Curving striped skyscraper against a pale blue sky"></div>
</section>

<section class="values">
  <div class="abs tag">
    <svg class="hex" viewBox="0 0 46 50"><polygon points="23,2 43,13.5 43,36.5 23,48 3,36.5 3,13.5" fill="none" stroke="#cfe0f1" stroke-width="2"/><path d="M15 21h16l-8 11z M15 21l4-4h8l4 4" fill="var(--accent)"/></svg>
    <span>/ Corporate Values</span>
  </div>
  <h2 class="abs lead">Behind our driven strategy for success</h2>
  <div class="abs ring-outer"></div>
  <div class="abs ring-inner"></div>
  <div class="abs ring-name">Tern Harbor<br>Equity</div>

  <div class="abs value left" style="right:783px;top:285px"><span>Advanced Technology</span>
    <svg viewBox="0 0 72 78"><polygon points="36,3 68,21 68,57 36,75 4,57 4,21" fill="#0b4a7f" stroke="#fff" stroke-width="5"/><rect x="24" y="28" width="24" height="16" fill="none" stroke="#fff" stroke-width="2.5"/><line x1="20" y1="48" x2="52" y2="48" stroke="#fff" stroke-width="2.5"/></svg></div>
  <div class="abs value left" style="right:817px;top:422px"><span>Outstanding Team</span>
    <svg viewBox="0 0 72 78"><polygon points="36,3 68,21 68,57 36,75 4,57 4,21" fill="#0b4a7f" stroke="#fff" stroke-width="5"/><circle cx="27" cy="32" r="4" fill="#fff"/><circle cx="36" cy="30" r="4" fill="#fff"/><circle cx="45" cy="32" r="4" fill="#fff"/><path d="M21 46q6-9 15-9t15 9z" fill="#fff"/></svg></div>
  <div class="abs value left" style="right:783px;top:560px"><span>Great Investment Products</span>
    <svg viewBox="0 0 72 78"><polygon points="36,3 68,21 68,57 36,75 4,57 4,21" fill="#0b4a7f" stroke="#fff" stroke-width="5"/><circle cx="36" cy="39" r="13" fill="#fff"/><text x="36" y="45" text-anchor="middle" font-family="Outfit,sans-serif" font-size="16" font-weight="600" fill="#0b4a7f">£</text></svg></div>

  <div class="abs value" style="left:781px;top:285px">
    <svg viewBox="0 0 72 78"><polygon points="36,3 68,21 68,57 36,75 4,57 4,21" fill="#0b4a7f" stroke="#fff" stroke-width="5"/><rect x="26" y="25" width="20" height="26" fill="none" stroke="#fff" stroke-width="2.5"/><circle cx="37" cy="40" r="5" fill="none" stroke="#fff" stroke-width="2.5"/><line x1="40" y1="44" x2="46" y2="50" stroke="#fff" stroke-width="2.5"/></svg><span>Comprehensive Analysis</span></div>
  <div class="abs value" style="left:817px;top:422px">
    <svg viewBox="0 0 72 78"><polygon points="36,3 68,21 68,57 36,75 4,57 4,21" fill="#0b4a7f" stroke="#fff" stroke-width="5"/><rect x="22" y="27" width="28" height="19" fill="none" stroke="#fff" stroke-width="2.5"/><rect x="28" y="37" width="4" height="6" fill="#fff"/><rect x="34" y="33" width="4" height="10" fill="#fff"/><rect x="40" y="31" width="4" height="12" fill="#fff"/><line x1="36" y1="46" x2="36" y2="53" stroke="#fff" stroke-width="2.5"/></svg><span>Notable Expertise</span></div>
  <div class="abs value" style="left:781px;top:560px">
    <svg viewBox="0 0 72 78"><polygon points="36,3 68,21 68,57 36,75 4,57 4,21" fill="#0b4a7f" stroke="#fff" stroke-width="5"/><circle cx="36" cy="39" r="13" fill="none" stroke="#fff" stroke-width="3"/><path d="M36 39V26a13 13 0 0 1 13 13z" fill="#fff"/><path d="M36 39l9 9" stroke="#fff" stroke-width="3"/></svg><span>Excellence in Risk Management</span></div>
</section>

<section class="mission">
  <div class="abs tag">
    <svg class="hex" viewBox="0 0 46 50"><polygon points="23,2 43,13.5 43,36.5 23,48 3,36.5 3,13.5" fill="var(--frost)" stroke="var(--mist)" stroke-width="2"/><path d="M13 25l8-7v14z M33 25l-8-7v14z" fill="var(--accent)"/></svg>
    <span>/ Mission</span>
  </div>
  <h2 class="abs lead">Our mission is to empower Dunmore College alumni graduates by establishing an investment fund and invest in multiple businesses.</h2>
  <div class="abs photo-c" role="img" aria-label="Businessman touching a glowing digital market data screen"></div>
  <div class="abs photo-d" role="img" aria-label="Hands holding a smartphone over rising bar chart graphics"></div>
</section>

<section class="contact">
  <div class="abs" style="inset:0;background:linear-gradient(180deg,rgba(40,70,110,.4),rgba(20,45,80,.5))" role="img" aria-label="Night city skyline seen from above, tinted navy"></div>
  <div class="abs tag">
    <svg class="hex" viewBox="0 0 46 50"><polygon points="23,2 43,13.5 43,36.5 23,48 3,36.5 3,13.5" fill="#1b3556" stroke="#cfe0f1" stroke-width="2"/><rect x="13" y="17" width="20" height="15" rx="2" fill="var(--accent)"/><path d="M13 18l10 8 10-8" fill="none" stroke="#fff" stroke-width="1.5"/></svg>
    <span>/ Contact Us</span>
  </div>
  <h2 class="abs lead">Send a message</h2>
  <div class="abs field" style="left:212px;top:273px;width:389px">Name</div>
  <div class="abs field" style="left:609px;top:273px;width:379px">Email</div>
  <div class="abs field" style="left:212px;top:334px;width:389px">Telephone</div>
  <div class="abs field" style="left:609px;top:334px;width:379px">Subject</div>
  <div class="abs field msg" style="left:212px;top:393px;width:776px">Message</div>
  <div class="abs btn-solid">Submit</div>
</section>

<footer class="site-footer">
  <div class="abs brand"><span class="brand-mark"></span><span>Tern Harbor<br>Equity</span></div>
  <div class="abs f-social"><span></span><span></span><span></span></div>
  <div class="abs f-col" style="left:439px;top:111px;width:125px">
    <h4>Navigation</h4>
    <ul><li>Home</li><li>Background</li><li>Advisory Board</li><li>Investment</li><li>Contact</li></ul>
  </div>
  <div class="abs f-col" style="left:595px;top:111px;width:190px">
    <h4>Contact</h4>
    <div class="f-row"><svg width="9" height="11" viewBox="0 0 9 11"><path d="M4.5 11S0 6.5 0 4.5a4.5 4.5 0 0 1 9 0C9 6.5 4.5 11 4.5 11z" fill="#9dbbdc"/><circle cx="4.5" cy="4.5" r="1.6" fill="#0b4a7f"/></svg><p>Tern Harbor Equity<br>418 Saltmarsh Row, Suite #300<br>Marlow Bay, ST 10198</p></div>
    <div class="f-row"><svg width="10" height="10" viewBox="0 0 10 10"><path d="M2 0l2 2.5-1.2 1.3a6 6 0 0 0 3.4 3.4L7.5 6 10 8l-1.5 2C4 10 0 6 0 1.5z" fill="#9dbbdc"/></svg><p>1800.555.0142</p></div>
    <div class="f-row"><svg width="11" height="8" viewBox="0 0 11 8"><rect width="11" height="8" fill="#9dbbdc"/><path d="M0 0l5.5 4.5L11 0" fill="none" stroke="#0b4a7f"/></svg><p>info@ternharborequity.com</p></div>
  </div>
  <div class="abs f-col" style="left:857px;top:111px;width:190px">
    <h4 style="border:none;padding-bottom:0">Subscribe for Newsletter</h4>
    <p>Enter your email address below to receive the latest updates from Tern Harbor Equity</p>
    <div class="subscribe"><span>Email address</span><svg width="12" height="9" viewBox="0 0 12 9"><path d="M0 4.5h11M7 1l4 3.5L7 8" fill="none" stroke="#cfe0f1"/></svg></div>
  </div>
  <div class="abs f-rule"></div>
  <div class="abs to-top"><svg width="12" height="16" viewBox="0 0 12 16"><path d="M6 16V1M1 6l5-5 5 5" fill="none" stroke="#cfe0f1" stroke-width="1.4"/></svg></div>
  <div class="abs copyright">© COPYRIGHT 2024 TERN HARBOR EQUITY | ALL RIGHTS RESERVED</div>
</footer>

</body>
</html>
```